Veloran Dental Development - Business Cards

We are a Dental Development and Management company. We are looking to develop a new business card design. We are business professional but modern. The logo that I have attached is the business colors. You can also check out our website for further detail. www.veloranmgmt-example.com

Target Market(s)

Dental Professionals, Dentists and Office Staff, Marketing Professionals

Industry/Entity Type

Business

Requirements
Must have
• Name - Bartholomew K. Tressing
Title - Marketing Director
Phone - 555-019-4827
Cell - 555-019-4827
Email - Bart.t@veloran-example.com
Address - 2917 W Larkmoor Rd, Mesa, AZ 85209
Web- www.veloran-example.com

Veloran Logo must go on the front. The other logos go on the back as affiliated businesses

Must be editable to enter specific Names, Positions, Phone numbers and email later on. Using Adobe CS5 currently.

```html
<!DOCTYPE html>
<html lang="en">
<head>
<meta charset="utf-8">
<title>Veloran Dental Development – Business Cards</title>
<link rel="stylesheet" href="https://fonts.googleapis.com/css2?family=Cinzel:wght@600&family=Roboto:wght@400;500;700&display=swap">
<style>
  :root {
    --page-bg: #e9e6e1;
    --orange-light: #f4b548;
    --orange-deep: #e39a25;
    --navy: #1f2a6e;
    --navy-card: #0d1a47;
    --white: #ffffff;
    --cross-red: #e0262b;
    --sprout-blue: #29a8e0;
  }
  * { box-sizing: border-box; margin: 0; padding: 0; }
  html, body {
    width: 1200px; height: 900px; overflow: hidden;
    background: var(--page-bg);
    font-family: "Roboto", Arial, sans-serif;
  }
  .sheet {
    position: relative; width: 1200px; height: 900px;
    display: flex; align-items: center; justify-content: center; gap: 60px;
  }
  .card {
    position: relative; width: 525px; height: 300px;
    border-radius: 4px; overflow: hidden;
    box-shadow: 0 10px 24px rgba(0,0,0,.22);
  }
  /* Front */
  .card--front {
    background: linear-gradient(160deg, var(--orange-light) 0%, var(--orange-deep) 100%);
    color: var(--white);
  }
  .brand {
    position: absolute; left: 32px; top: 34px;
    display: flex; align-items: center; gap: 12px;
  }
  .brand__dot {
    width: 34px; height: 34px; border-radius: 50%; background: var(--white);
  }
  .brand__name {
    font-family: "Cinzel", Georgia, serif; font-weight: 600;
    font-size: 22px; line-height: 1.1; color: var(--navy);
    letter-spacing: .5px;
  }
  .person { position: absolute; left: 32px; top: 120px; }
  .person__name { font-size: 22px; font-weight: 700; color: var(--navy); }
  .person__title { font-size: 15px; margin-top: 4px; }
  .contact {
    position: absolute; left: 32px; top: 178px;
    list-style: none; font-size: 15px; line-height: 24px;
  }
  .contact li { display: flex; align-items: center; gap: 10px; }
  .contact svg { width: 13px; height: 13px; fill: var(--navy); flex: none; }
  /* Back */
  .card--back { background: var(--navy-card); color: var(--white); }
  .affiliate-rapid {
    position: absolute; left: 200px; top: 88px;
    display: flex; align-items: center; gap: 12px;
  }
  .affiliate-rapid__mark { width: 40px; height: 40px; background: var(--cross-red); }
  .affiliate-rapid__name {
    font-size: 22px; font-weight: 500; color: var(--cross-red); line-height: 1.1;
  }
  .affiliate-sprout {
    position: absolute; left: 40px; top: 180px;
    display: flex; align-items: center; gap: 10px;
  }
  .affiliate-sprout__mark { width: 34px; height: 34px; border-radius: 50%; background: var(--sprout-blue); }
  .affiliate-sprout__name { font-size: 16px; font-weight: 500; color: var(--sprout-blue); }
  .back__web {
    position: absolute; right: 32px; bottom: 30px;
    font-size: 15px; letter-spacing: .3px;
  }
</style>
</head>
<body>
<main class="sheet">
  <section class="card card--front" aria-label="Business card front">
    <div class="brand">
      <span class="brand__dot"></span>
      <span class="brand__name">Veloran<br>Dental Development</span>
    </div>
    <div class="person">
      <p class="person__name">Bartholomew K. Tressing</p>
      <p class="person__title">Marketing Director</p>
    </div>
    <ul class="contact">
      <li><svg viewBox="0 0 16 16"><path d="M8 1 1 7h2v8h4v-5h2v5h4V7h2z"/></svg>Address - 2917 W Larkmoor Rd, Mesa, AZ 85209</li>
      <li><svg viewBox="0 0 16 16"><path d="M4 0h8v16H4zM5.5 2v10h5V2z"/></svg>555-019-4827</li>
      <li><svg viewBox="0 0 16 16"><path d="M0 3h16v10H0zM1.5 4.5 8 9l6.5-4.5z"/></svg>Bart.t@veloran-example.com</li>
      <li><svg viewBox="0 0 16 16"><path d="M3 1c2 0 3 3 2 4l-1 1c1 2 3 4 5 5l1-1c1-1 4 0 4 2s-2 3-3 3C6 15 1 10 1 4c0-1 1-3 2-3z"/></svg>555-019-4827</li>
    </ul>
  </section>

  <section class="card card--back" aria-label="Business card back">
    <div class="affiliate-rapid">
      <span class="affiliate-rapid__mark"></span>
      <span class="affiliate-rapid__name">Rapidcare<br>Dental Centers</span>
    </div>
    <div class="affiliate-sprout">
      <span class="affiliate-sprout__mark"></span>
      <span class="affiliate-sprout__name">Brightsprout Pediatric Dental</span>
    </div>
    <p class="back__web">www.veloran-example.com</p>
  </section>
</main>
</body>
</html>
```